Business Card Design Project

We require a business card template to cover basic contact information - our company logo, names of employees, title, mobile and email.

Target Market(s)

Corporate

Industry/Entity Type

Business

Font styles to use
Sans Serif

Requirements
Nice to have
• Thinking it would be great just to have the logo taking up approximately half the space (so it goes as far across the top of the card as possible) and then contact details in the lower half of the card. Keen just to use only the two colours in the logo, on a white background.
Should not have
• No fussy drawings

```html
<!DOCTYPE html>
<html lang="en">
<head>
<meta charset="utf-8">
<title>Tidewell Developments – Business Card</title>
<link rel="stylesheet" href="https://fonts.googleapis.com/css2?family=Arimo:wght@400&display=swap">
<style>
  :root {
    --turquoise: #4fe3cc;
    --navy: #0d1a7a;
    --edge-red: #7d2a22;
    --icon-white: #f4f1f1;
    --rule-red: #e0604a;
  }
  html, body {
    margin: 0;
    padding: 0;
    overflow: hidden;
    background: #ffffff;
  }
  .card {
    position: relative;
    width: 1200px;
    height: 722px;
    overflow: hidden;
    font-family: "Arimo", Arial, sans-serif;
    background:
      radial-gradient(ellipse 520px 380px at 360px 400px, rgba(243,228,228,0.95) 0%, rgba(243,228,228,0) 100%),
      radial-gradient(ellipse 420px 360px at 800px 380px, rgba(211,212,188,0.9) 0%, rgba(211,212,188,0) 100%),
      radial-gradient(ellipse 760px 520px at 560px 380px, #e4cac6 0%, #c49a90 50%, #9a5a4c 78%, var(--edge-red) 100%);
  }
  .company-name {
    position: absolute;
    left: 275px;
    top: 112px;
    width: 538px;
    height: 181px;
    display: flex;
    align-items: center;
    justify-content: center;
    margin: 0;
    color: var(--navy);
    font-size: 52px;
    font-weight: 400;
    line-height: 1;
    white-space: nowrap;
  }
  .divider {
    position: absolute;
    left: 427px;
    top: 310px;
    width: 357px;
    height: 3px;
    background: linear-gradient(90deg, rgba(224,96,74,0) 0%, var(--rule-red) 40%, var(--rule-red) 60%, rgba(224,96,74,0) 100%);
    box-shadow: 0 4px 6px rgba(60,30,30,0.35);
  }
  .employee {
    position: absolute;
    left: 0;
    top: 340px;
    width: 1176px;
    text-align: center;
  }
  .employee-name {
    display: block;
    color: var(--turquoise);
    font-size: 50px;
    line-height: 56px;
  }
  .employee-title {
    display: block;
    margin-top: 4px;
    color: var(--navy);
    font-size: 23px;
    line-height: 28px;
  }
  .contacts {
    position: absolute;
    left: 362px;
    top: 472px;
    margin: 0;
    padding: 0;
    list-style: none;
  }
  .contact {
    display: flex;
    align-items: center;
    height: 51px;
    color: var(--navy);
    font-size: 24px;
  }
  .contact-icon {
    width: 34px;
    height: 34px;
    margin-right: 66px;
  }
</style>
</head>
<body>
  <main class="card">
    <h1 class="company-name">Tidewell Developments</h1>

    <div class="divider"></div>

    <div class="employee">
      <span class="employee-name">Emp.Name</span>
      <span class="employee-title">(Title)</span>
    </div>

    <ul class="contacts">
      <li class="contact">
        <svg class="contact-icon" viewBox="0 0 34 34" aria-hidden="true">
          <circle cx="17" cy="17" r="14" fill="none" stroke="var(--icon-white)" stroke-width="2"/>
          <path d="M13 9 q-4 3 -1 10 q3 6 8 7 l2 -3 l-3 -3 l-2 1 q-3 -3 -3 -6 l2 -1 l-1 -4 z" fill="var(--icon-white)"/>
        </svg>
        <span>0987 654 321</span>
      </li>
      <li class="contact">
        <svg class="contact-icon" viewBox="0 0 34 34" aria-hidden="true">
          <rect x="3" y="9" width="28" height="18" fill="var(--icon-white)"/>
          <path d="M3 9 L17 20 L31 9 M3 27 L13 17 M31 27 L21 17" fill="none" stroke="#b9aaa8" stroke-width="1.2"/>
        </svg>
        <span>name@tidewell.com</span>
      </li>
      <li class="contact">
        <svg class="contact-icon" viewBox="0 0 34 34" aria-hidden="true">
          <rect x="4" y="6" width="26" height="18" rx="1" fill="var(--icon-white)"/>
          <rect x="7" y="9" width="20" height="12" fill="#c9b9b6"/>
          <rect x="14" y="24" width="6" height="4" fill="var(--icon-white)"/>
          <rect x="10" y="28" width="14" height="2" fill="var(--icon-white)"/>
        </svg>
        <span>www.tidewell.com</span>
      </li>
    </ul>
  </main>
</body>
</html>
```